Valdorick Business Card Design

Valdorick is the holdings company for my portfolio of businesses. These businesses currently only include Valdorick Advising. V|A is a strategic consulting firm that focuses on small businesses and start-ups that want help with their brand. We focus on partnering with influencers (Pro Athletes and Celebrities) and Social Media Marketing. We also want to focus on companies that have a positive effect on the community or world. The audience I am going after is very corporate. I want to have the corporate edge with some 25yr old flair.
Industry/Entity Type
Business
Contact Information for Business Card
General Idea AttachedLogo (Attached)Jonathan R. MasonCEO & Managing MemberDown Left Bottom CornerPhone: 347-570-0585Cell: 240-604-7930mason@valdorick-example.comDown Right Bottom Corner 174 W 4th St, Ste 212New York, NY 10014www.valdorick-example.comBackside LogoI want the entire card extra thick and with metallic finish
Look and feel

```html
<!DOCTYPE html>
<html lang="en">
<head>
<meta charset="utf-8">
<title>Valdorick Holdings – Business Card</title>
<link href="https://fonts.googleapis.com/css2?family=Cinzel:wght@500&family=Open+Sans:wght@400;600&display=swap" rel="stylesheet">
<style>
  :root {
    --brand-red: #ad0019;
    --brand-grey: #6b6b6d;
    --ink: #3c3c3e;
    --paper: #ffffff;
    --paper-shade: #e6e6e8;
    --stage: #ecebe8;
  }
  * { margin: 0; padding: 0; box-sizing: border-box; }
  html, body { width: 1200px; height: 899px; overflow: hidden; }
  body {
    background: var(--stage);
    font-family: "Open Sans", Arial, sans-serif;
    position: relative;
  }
  .card {
    position: absolute;
    left: 290px;
    width: 620px;
    height: 354px;
    background: radial-gradient(ellipse at 40% 30%, var(--paper) 0%, var(--paper) 45%, var(--paper-shade) 100%);
    box-shadow: 0 6px 18px rgba(0,0,0,0.18);
    overflow: hidden;
  }
  .card--back { top: 70px; }
  .card--front { top: 468px; }

  .wordmark {
    font-family: "Cinzel", Georgia, serif;
    font-weight: 500;
    color: var(--brand-red);
    line-height: 1;
  }
  .card--back .wordmark {
    position: absolute;
    left: 40px;
    bottom: 48px;
    font-size: 30px;
  }
  .wordmark__suffix { font-size: 0.55em; margin-left: 6px; }

  .logo-block {
    position: absolute;
    left: 70px;
    top: 78px;
    display: flex;
    flex-direction: column;
    align-items: center;
    gap: 14px;
  }
  .logo-block__square {
    width: 62px;
    height: 62px;
    background: var(--brand-red);
  }
  .logo-block .wordmark { font-size: 24px; }

  .contact {
    position: absolute;
    left: 372px;
    top: 40px;
    padding-left: 14px;
    border-left: 1px solid var(--brand-grey);
    font-size: 12.5px;
    line-height: 1.45;
    color: var(--ink);
  }
  .contact__row { display: flex; align-items: center; gap: 5px; }
  .contact__icon { width: 11px; height: 11px; fill: var(--brand-red); flex: none; }

  .swoosh { position: absolute; inset: 0; width: 620px; height: 354px; }

  .holder {
    position: absolute;
    left: 0;
    width: 480px;
    bottom: 18px;
    text-align: center;
    color: var(--paper);
    font-size: 13px;
    letter-spacing: 2.5px;
  }
</style>
</head>
<body>

  <section class="card card--back" aria-label="Card back">
    <div class="wordmark">Valdorick Holdings<span class="wordmark__suffix">LLC</span></div>
  </section>

  <section class="card card--front" aria-label="Card front">
    <svg class="swoosh" viewBox="0 0 620 354" aria-hidden="true">
      <path d="M30 292 C 230 262, 460 228, 620 128 L620 142 C 470 240, 260 272, 30 292 Z" fill="var(--brand-grey)"/>
      <path d="M0 312 C 220 286, 470 250, 620 156 L620 354 L0 354 Z" fill="var(--brand-red)"/>
    </svg>

    <div class="logo-block">
      <div class="logo-block__square"></div>
      <div class="wordmark">Valdorick Holdings<span class="wordmark__suffix">LLC</span></div>
    </div>

    <address class="contact" style="font-style:normal">
      <div>041.12th floor,Grove</div>
      <div>Parkside Road LKG</div>
      <div class="contact__row">
        <svg class="contact__icon" viewBox="0 0 24 24"><path d="M6.6 10.8a15.1 15.1 0 0 0 6.6 6.6l2.2-2.2a1 1 0 0 1 1-.25 11.4 11.4 0 0 0 3.6.57 1 1 0 0 1 1 1V20a1 1 0 0 1-1 1A17 17 0 0 1 3 4a1 1 0 0 1 1-1h3.5a1 1 0 0 1 1 1c0 1.25.2 2.45.57 3.57a1 1 0 0 1-.25 1z"/></svg>
        <span>012 555 0147</span>
      </div>
      <div class="contact__row">
        <svg class="contact__icon" viewBox="0 0 24 24"><path d="M2 5h20v14H2z M2 5l10 8 10-8" stroke="#fff" stroke-width="1.5"/></svg>
        <span>you@mailbox-example.com</span>
      </div>
      <div class="contact__row">
        <svg class="contact__icon" viewBox="0 0 24 24"><circle cx="12" cy="12" r="10"/><path d="M2 12h20M12 2c3 3 3 17 0 20M12 2c-3 3-3 17 0 20" stroke="#fff" stroke-width="1.4" fill="none"/></svg>
        <span>www.yoursite-example.com</span>
      </div>
    </address>

    <p class="holder">MARCUS ELLERY Managing Director</p>
  </section>

</body>
</html>
```